Purchasing Management Consulting B to B Web Design PAYMENT GUARANTY

We'd like to build a new digital image for our website.

Our company is managing purchasing consultancy services for Large and Medium companies around 4 activities :
- Procurement outsourcing
- Purchasing consulting (cost reduction)
- Supply chain training
- Web platform to manage Supplier risk (TrusoMark.com)

We now aim to harmonies our website in term of design in order to build a strongest Corporate Image.

SEE REQUIREMENT ENCLOSED

Please have a look on our current websites:
- www.procuvantix.com
- www.pqz-network.com
- www.trusomark.com

Reason: Hello, Some project received are not really professional and need more details. I did not see all deliverable requested in specifications. I'll revert to designer to improve design. Regards, Bastien

Reason: Only few designers reply and feedback still need to be done.

Target Market(s)

Our business is exclusively Business to Business toward Medium and Large companies.

Industry/Entity Type

Digital

Requirements
Must have
• Website will be developped in Joomla CMS.
The user community will use Fellowkit module : Visitor should be "influenced" to communicate its contact details by registering the community.

Ergonomy, Simplicity and professionnalism is the key objectives.

Deliverables :
- Corporate Home page including clear access to our 4 activities
- Dynamique banner
- Corporate article / contact pages (1 or 2)
- Activities home pages (x 4)
- Activity Catalog (Indesign for paper version)
Nice to have
• Integration of Design for our consulting and training catalog will be interesting.

Livechat design (the one of Craftplaza.com is good)
Should not have
• Only psd

Not html

```html
<!DOCTYPE html>
<html lang="fr">
<head>
<meta charset="utf-8">
<title>PVX Consulting – Accueil</title>
<link rel="stylesheet" href="https://fonts.googleapis.com/css2?family=Roboto+Condensed:wght@400;700&family=Roboto:wght@400;500&display=swap">
<style>
:root{
  --lime:#c5c90b;
  --lime-dark:#a5a900;
  --lime-text:#9a9e00;
  --amber:#e0a817;
  --amber-light:#f1c65c;
  --amber-bar:#f6c648;
  --ink:#3a3a3a;
  --grey:#6f6f6f;
  --panel:#f2f2f2;
  --line:#dcdcdc;
  --ref-blue:#2a3a8a;
  --white:#ffffff;
}
*{box-sizing:border-box;margin:0;padding:0}
html,body{width:1200px;height:1100px;overflow:hidden;background:var(--white)}
body{position:relative;font-family:"Roboto",Arial,sans-serif;color:var(--ink)}
.abs{position:absolute}
.top-rule{left:0;top:0;width:1200px;height:5px;background:var(--lime)}

/* brand */
.brand{left:118px;top:28px;width:180px;height:136px;display:flex;align-items:center;gap:10px}
.brand-dot{width:58px;height:58px;border-radius:50%;background:var(--lime)}
.brand-name{font-family:"Roboto Condensed",sans-serif;font-weight:700;font-size:26px;color:var(--grey);line-height:1.05}

/* language */
.lang{left:949px;top:22px;width:127px;height:36px;border:2px solid #e3e3e3;display:flex;align-items:center;padding-left:8px;gap:10px;font-size:12px;color:#555}
.flag{display:flex;width:20px;height:14px}
.flag i{flex:1}
.caret{margin-left:auto;margin-right:14px;width:0;height:0;border-left:5px solid transparent;border-right:5px solid transparent;border-top:8px solid #555}

/* nav */
.nav{left:302px;top:73px;width:776px;height:43px;background:linear-gradient(#f8d068,var(--amber-bar));display:flex;justify-content:flex-end;align-items:center;padding-right:32px}
.nav a{font-family:"Roboto Condensed",sans-serif;font-size:16px;color:#5a4a1a;text-decoration:none;margin-left:46px}

/* login */
.login-label{top:140px;font-family:"Roboto Condensed",sans-serif;font-size:11px;line-height:13px;color:#444;font-weight:700}
.field{top:131px;width:143px;height:30px;border:2px solid #e3e3e3}
.btn-ok{width:43px;height:30px;background:#616161;color:#fff;font-family:"Roboto Condensed",sans-serif;font-weight:700;font-size:14px;display:flex;align-items:center;justify-content:center;border-top:1px solid #888}

/* activities band */
.band-head{left:119px;top:188px;width:960px;height:78px;background:var(--amber);color:#fff;font-family:"Roboto Condensed",sans-serif;font-weight:700;font-size:30px;display:flex;align-items:center;justify-content:center}
.band{left:119px;top:266px;width:960px;height:117px;background:var(--amber-light);border-bottom:5px solid var(--amber)}
.activity{position:absolute;top:16px;width:160px;text-align:center;font-family:"Roboto Condensed",sans-serif;font-weight:700;font-size:17px;color:#3a2e10}
.activity .icon{width:50px;height:52px;margin:0 auto 14px;border-radius:10px}

/* hero */
.hero{left:119px;top:394px;width:960px;height:350px;background:linear-gradient(90deg,#cfd21a,var(--lime) 60%,#c0c400)}
.hero-art{left:140px;top:408px;width:392px;height:328px;border-radius:6px;background:radial-gradient(ellipse at 50% 60%,#e8e9a8,#cacd2e 75%)}
.hero-title{left:565px;top:466px;font-family:"Roboto Condensed",sans-serif;font-weight:700;font-size:52px;color:#fff;text-shadow:0 2px 3px rgba(0,0,0,.35)}
.hero-copy{left:569px;top:560px;width:486px;font-family:"Roboto Condensed",sans-serif;font-weight:700;font-size:13.5px;letter-spacing:.35px;line-height:21px;color:#fff;text-align:justify}
.dots{left:1022px;top:720px;display:flex;gap:4px}
.dots i{width:8px;height:8px;border-radius:50%;background:#a9ad00}

/* columns */
.col-title{top:764px;font-family:"Roboto Condensed",sans-serif;font-size:18px;font-weight:400;color:#444}
.arrows{top:768px;display:flex;gap:2px}
.arrows i{width:15px;height:15px;border-radius:50%;background:var(--lime-dark);display:block;position:relative}
.arrows i::after{content:"";position:absolute;top:4px;left:5px;border-top:3.5px solid transparent;border-bottom:3.5px solid transparent;border-left:5px solid #fff}
.arrows i.prev::after{left:4px;border-left:0;border-right:5px solid #fff}
.card{top:799px;width:230px;height:169px;background:linear-gradient(#fafafa,var(--panel));border:1px solid var(--line);font-size:12px;line-height:14.5px;color:#555;padding:14px 5px}
.link{color:var(--lime-text);font-family:"Roboto Condensed",sans-serif;font-size:12px;line-height:16px}
.thumb{float:left;width:72px;height:72px;margin:-2px 8px 6px -1px;background:linear-gradient(135deg,#e9a84c,#6aa8d4,#9bc44a)}
.date{font-family:"Roboto Condensed",sans-serif;font-size:12px;color:#555;margin-top:14px}
.justify{text-align:justify;clear:both}
.ref-name{margin:22px auto 0;height:76px;display:flex;align-items:center;justify-content:center;gap:8px;font-family:"Roboto Condensed",sans-serif;font-weight:700;font-size:26px;color:var(--ref-blue)}
.ref-name span{width:14px;height:14px;border-radius:50%;background:var(--ref-blue)}
.email{width:214px;height:31px;background:#fff;border:2px solid #e3e3e3;font-size:11px;color:#555;padding:7px 6px;margin:20px 0 0 3px}
.news-ok{margin:11px 0 0 174px}
.social{display:flex;gap:4px;justify-content:center;margin-top:22px}
.social i{width:27px;height:27px;border-radius:50%;background:#9a9a9a}

/* footer */
.foot-rule{left:119px;top:1016px;width:963px;height:1px;background:var(--lime-dark)}
.foot-brand{left:118px;top:1028px;display:flex;align-items:center;gap:6px;font-family:"Roboto Condensed",sans-serif;font-weight:700;font-size:14px;color:#8a8a8a}
.foot-brand span{width:28px;height:28px;border-radius:50%;background:#bdbdbd}
.foot-links{right:122px;top:1043px;font-size:12px;color:#555}
.foot-links b{font-weight:400;margin:0 6px}
</style>
</head>
<body>
<div class="abs top-rule"></div>

<div class="abs brand"><span class="brand-dot"></span><span class="brand-name">PVX<br>Consulting</span></div>

<div class="abs lang"><span class="flag"><i style="background:#22408c"></i><i style="background:#fff"></i><i style="background:#d52b2b"></i></span>FRENCH<span class="caret"></span></div>

<nav class="abs nav">
  <a href="#">ACCUEIL</a><a href="#">PROCUVANTIX</a><a href="#">MÉTIERS</a><a href="#">NOS RÉFÉRENCES</a><a href="#">CONTACT</a>
</nav>

<span class="abs login-label" style="left:572px">UTILISATEUR</span>
<span class="abs field" style="left:645px"></span>
<span class="abs login-label" style="left:797px">MOT DE PASSE</span>
<span class="abs field" style="left:880px"></span>
<span class="abs btn-ok" style="left:1035px;top:131px">OK</span>

<div class="abs band-head">ACHETEZ EN TOUTE SIMPLICITE</div>
<div class="abs band">
  <div class="activity" style="left:32px"><div class="icon" role="img" aria-label="Icône communauté" style="background:linear-gradient(#e98b4b,#5aa0d8)"></div>COMMUNAUTE</div>
  <div class="activity" style="left:229px"><div class="icon" role="img" aria-label="Icône consulting" style="background:linear-gradient(#f0a23c,#c8c8c8)"></div>CONSUITING</div>
  <div class="activity" style="left:413px"><div class="icon" role="img" aria-label="Icône formation" style="background:linear-gradient(#f4f4f4,#c9a06a)"></div>FORMATION</div>
  <div class="activity" style="left:591px"><div class="icon" role="img" aria-label="Icône veille légale" style="background:linear-gradient(#7ab8e0,#5d9a3c)"></div>TRUSOMARK</div>
  <div class="activity" style="left:773px"><div class="icon" role="img" aria-label="Icône multi-devis" style="background:linear-gradient(#f0a23c,#3aa3a0)"></div>MULTI-DEVIS</div>
</div>

<div class="abs hero"></div>
<div class="abs hero-art" role="img" aria-label="Illustration de figurines colorées avec bulles de dialogue"></div>
<h1 class="abs hero-title">COMMUNAUTE</h1>
<p class="abs hero-copy">LOREM IPSUM DOLOR SIT AMET, CONSECTETUR ADIPISICING ELIT, SED DO EIUSMOD TEMPOR INCIDIDUNT UT LABORE ET DOLORE MAGNA ALIQUA. UT ENIM AD MINIM VENIAM, QUIS NOSTRUD EXERCITATION ULLAMCO LABORIS NISI UT ALIQUIP EX EA COMMODO CONSEQUAT. DUIS AUTE IRURE DOLOR IN REPREHENDERIT IN VOLUP-TATE VELIT ESSE C</p>
<div class="abs dots"><i></i><i></i><i></i></div>

<h2 class="abs col-title" style="left:120px">ACTUALITES</h2>
<div class="abs arrows" style="left:318px"><i class="prev"></i><i></i></div>
<h2 class="abs col-title" style="left:364px">PROCUVANTIX</h2>
<div class="abs arrows" style="left:578px"><i></i></div>
<h2 class="abs col-title" style="left:608px">NOS REFERENCES</h2>
<div class="abs arrows" style="left:806px"><i class="prev"></i><i></i></div>
<h2 class="abs col-title" style="left:851px">NEWSLETTER</h2>

<div class="abs card" style="left:120px">
  <div class="thumb" role="img" aria-label="Illustration d'actualité, personnages en réseau"></div>
  <div class="link">Lorem ipsum dolor sit amet, consectetur a</div>
  <div class="date">April 15, 2013</div>
  <p class="justify">Lorem ipsum dolor sit amet, consectetur adipisicing elit, sed do eiusmod tempor incididunt ut labore et dolore magna aliqua. Ut enim ad minim veniam,</p>
</div>

<div class="abs card" style="left:364px">
  <div class="link">Lorem ipsum dolor sit amet, consectetur a</div>
  <p class="justify" style="margin-top:10px">Lorem ipsum dolor sit amet, consectetur adipisicing elit, sed do eiusmod tempor incididunt ut labore et dolore magna aliqua. Ut enim ad minim veniam,</p>
  <p class="justify" style="margin-top:14px">sed do eiusmod tempor incididunt ut labore et dolore magna aliqua. Ut enim ad minim veniam,</p>
</div>

<div class="abs card" style="left:608px;text-align:center">
  <div class="ref-name"><span></span>Quorvane</div>
  <div class="link" style="margin-top:14px">Lorem ipsum dolor sit amet, consec-<br>tetur a</div>
</div>

<div class="abs card" style="left:851px">
  <div class="email">Inserter Email</div>
  <div class="btn-ok news-ok">OK</div>
  <div class="social"><i></i><i></i><i></i><i></i><i></i></div>
</div>

<div class="abs foot-rule"></div>
<div class="abs foot-brand"><span></span>PVX</div>
<div class="abs foot-links">Procuvantix<b>|</b>Recrutement<b>|</b>Presse<b>|</b>Mentions Légales<b>|</b>Nous contacter</div>
</body>
</html>
```